Marcus Tellow album cover "Borrowed Lanterns, Quiet Harbors"

3000x3000 album cover using attached image and provided text needed for cover of upcoming album for Seattle musician. Only front cover needed at this time.

Font styles to use
Serif
Sans Serif

Colors

Designer to choose colors to be used in the design.

```html
<!DOCTYPE html>
<html lang="en">
<head>
<meta charset="utf-8">
<title>Marcus Tellow – Borrowed Lanterns, Quiet Harbors</title>
<link rel="stylesheet" href="https://fonts.googleapis.com/css2?family=Exo+2:wght@700;800&family=Oswald:wght@600;700&family=Playfair+Display:wght@900&family=Russo+One&family=Stardos+Stencil:wght@700&display=swap">
<style>
  :root {
    --amber: #f5ad2e;
    --white: #ffffff;
    --ink: #0d0d0d;
    --backdrop: #e6e6e6;
    --night: #0b0d10;
  }
  html, body {
    margin: 0;
    width: 1200px;
    height: 907px;
    overflow: hidden;
    background: var(--backdrop);
  }
  .album-cover {
    position: absolute;
    left: 170px;
    top: 23px;
    width: 860px;
    height: 860px;
    overflow: hidden;
    background: var(--night);
  }
  .cover-photo {
    position: absolute;
    inset: 0;
    background:
      radial-gradient(ellipse 40% 30% at 28% 62%, rgba(226, 210, 182, 0.85), rgba(226, 210, 182, 0) 70%),
      radial-gradient(ellipse 45% 35% at 38% 30%, rgba(62, 84, 38, 0.9), rgba(62, 84, 38, 0) 75%),
      radial-gradient(ellipse 35% 25% at 20% 92%, rgba(94, 110, 60, 0.8), rgba(94, 110, 60, 0) 75%),
      radial-gradient(ellipse 40% 40% at 95% 92%, rgba(84, 122, 140, 0.75), rgba(84, 122, 140, 0) 75%),
      radial-gradient(ellipse 50% 18% at 25% 6%, rgba(255, 255, 255, 0.55), rgba(255, 255, 255, 0) 70%),
      radial-gradient(ellipse 30% 55% at 75% 55%, rgba(70, 70, 70, 0.6), rgba(70, 70, 70, 0) 75%),
      var(--night);
  }
  .cover-art {
    position: absolute;
    inset: 0;
  }
  .initial { font-family: "Playfair Display", Georgia, serif; font-weight: 900; fill: var(--white); }
  .name-top { font-family: "Oswald", "Arial Narrow", sans-serif; font-weight: 700; fill: var(--amber); }
  .name-bottom {
    font-family: "Russo One", "Arial Black", sans-serif;
    fill: var(--amber);
    stroke: var(--white);
    stroke-width: 6;
    paint-order: stroke;
  }
  .bar { opacity: 0.92; }
  .bar-light { fill: #ececec; }
  .bar-amber { fill: var(--amber); }
  .title-line { font-family: "Stardos Stencil", Georgia, serif; font-weight: 700; }
  .title-white { fill: var(--white); }
  .title-amber { fill: var(--amber); }
  .date-band { fill: var(--amber); }
  .date-frame { fill: none; stroke: var(--ink); stroke-width: 1.2; }
  .month-box { fill: var(--white); }
  .month { font-family: "Oswald", "Arial Narrow", sans-serif; font-weight: 700; fill: var(--ink); }
  .days { font-family: "Exo 2", Arial, sans-serif; font-weight: 800; fill: var(--white); }
  .at { font-family: "Exo 2", Arial, sans-serif; font-weight: 700; fill: var(--white); }
  .time { font-family: "Exo 2", Arial, sans-serif; font-weight: 800; fill: var(--ink); }
  .divider { stroke: var(--ink); stroke-width: 1.5; }
  .rule { fill: var(--white); }
</style>
</head>
<body>
  <main class="album-cover">
    <div class="cover-photo" role="img" aria-label="Night photo of a vintage camper trailer lit from inside in a leafy backyard under string lights, with a faint silhouette of a guitarist and drifting smoke"></div>

    <svg class="cover-art" width="860" height="860" viewBox="0 0 860 860">
      <rect class="rule" x="433" y="30" width="402" height="4" rx="2"/>

      <g class="artist-name">
        <text class="initial" x="292" y="338" font-size="400" textLength="146" lengthAdjust="spacingAndGlyphs">M</text>
        <text class="name-top" x="448" y="172" font-size="176" textLength="385" lengthAdjust="spacingAndGlyphs">ARCUS</text>
        <text class="name-bottom" x="450" y="336" font-size="200" textLength="382" lengthAdjust="spacingAndGlyphs">TELLOW</text>
      </g>

      <g class="bar-chart">
        <rect class="bar bar-light" x="470" y="402" width="65" height="250"/>
        <rect class="bar bar-amber" x="563" y="471" width="65" height="181"/>
        <rect class="bar bar-light" x="656" y="374" width="66" height="278"/>
        <rect class="bar bar-amber" x="750" y="427" width="65" height="225"/>
      </g>

      <g class="album-title">
        <text class="title-line title-white" x="451" y="720" font-size="50" textLength="385" lengthAdjust="spacingAndGlyphs">BORROWED</text>
        <text class="title-line title-amber" x="451" y="779" font-size="50" textLength="380" lengthAdjust="spacingAndGlyphs">LANTERNS,</text>
        <text class="title-line title-white" x="451" y="835" font-size="48" textLength="385" lengthAdjust="spacingAndGlyphs">QUIET HARBORS</text>
      </g>

      <g class="release-date">
        <rect class="date-band" x="0" y="737" width="430" height="97"/>
        <rect class="date-frame" x="137" y="745" width="285" height="81"/>
        <rect class="month-box" x="9" y="728" width="124" height="113"/>
        <text class="month" x="16" y="826" font-size="92" textLength="110" lengthAdjust="spacingAndGlyphs">JAN</text>
        <text class="days" x="149" y="806" font-size="60" textLength="142" lengthAdjust="spacingAndGlyphs">28-31</text>
        <line class="divider" x1="301" y1="756" x2="301" y2="812"/>
        <text class="at" x="343" y="781" font-size="34">at</text>
        <text class="time" x="314" y="818" font-size="42" textLength="96" lengthAdjust="spacingAndGlyphs">6:30</text>
      </g>
    </svg>
  </main>
</body>
</html>
```